Quorvane Stationery Design Project

We need stationary design that goes with the attached logo. We have logo in two different versions. One in Red/Black and the other in Blue/Green. Red/Black is going to be our primary color and we are planning to use Blue/Green occasionally as necessary.

So we need stationary design in both color combinations. Maybe you can work with Red/Black first and once we decide on the design, then you can show the Blue/Green variation.

Please see the attached png and psd files for logo.

Target Market(s)

IT departments of Medium size Enterprises.

Industry/Entity Type

Work

Requirements
Must have
• -Letter head
-Cover page design for white papers and articles that are going to publish
-Business Card
-Envelope design
Nice to have
• - High level design template that we can follow for our internal web applications

```html
<!DOCTYPE html>
<html lang="en">
<head>
<meta charset="utf-8">
<title>Quorvane Stationery</title>
<link rel="stylesheet" href="https://fonts.googleapis.com/css2?family=Open+Sans:wght@400;600;700&display=swap">
<style>
  :root {
    --ink: #1b1b1b;
    --red: #c8161d;
    --red-deep: #8f0f14;
    --paper: #ffffff;
    --stage: #ececec;
    --grey-text: #6b6b6b;
    --band-grey: #4a4a4a;
    --signature-tint: #dfe3f2;
  }
  * { box-sizing: border-box; margin: 0; padding: 0; }
  html, body { width: 1200px; height: 914px; overflow: hidden; }
  body {
    background: var(--stage);
    font-family: "Open Sans", Arial, sans-serif;
    color: var(--ink);
    position: relative;
  }
  .sheet {
    position: absolute;
    box-shadow: 0 6px 18px rgba(0,0,0,.14), 0 1px 3px rgba(0,0,0,.1);
  }
  .sheet--light { background: var(--paper); }
  .sheet--dark { background: var(--ink); color: #fff; }

  /* brand lockup */
  .brand { display: flex; align-items: center; gap: 7px; }
  .brand__mark { width: 12px; height: 12px; background: var(--red); flex: none; }
  .brand__name {
    font-weight: 700; letter-spacing: 3px; text-transform: uppercase;
    font-size: 15px; color: var(--ink); white-space: nowrap;
  }
  .sheet--dark .brand__name { color: #fff; }
  .brand--small .brand__mark { width: 8px; height: 8px; }
  .brand--small .brand__name { font-size: 10px; letter-spacing: 2px; }

  .contact-lines { font-size: 5.6px; line-height: 1.6; color: var(--grey-text); white-space: nowrap; }
  .web { color: var(--red); font-weight: 600; white-space: nowrap; }

  /* letterhead */
  .letterhead { left: 40px; top: 50px; width: 390px; height: 552px; padding: 46px 38px 0; }
  .letterhead__salutation { margin-top: 48px; font-size: 8px; font-weight: 700; }
  .letterhead__body { margin-top: 10px; font-size: 6.6px; line-height: 1.65; color: var(--grey-text); }
  .letterhead__body p + p { margin-top: 8px; }
  .letterhead__closing { margin-top: 18px; font-size: 6.6px; color: var(--grey-text); }
  .letterhead__signature { display: block; margin: 6px 0 4px; }
  .letterhead__signer { font-size: 8px; font-weight: 700; }
  .letterhead__footer {
    position: absolute; left: 38px; right: 38px; bottom: 34px;
    border-top: 1px solid var(--red); padding-top: 6px;
    display: flex; justify-content: space-between; align-items: flex-end;
  }
  .letterhead__footer .web { font-size: 5.6px; }

  /* cover page */
  .cover { left: 460px; top: 50px; width: 390px; height: 552px; overflow: hidden; }
  .cover__brand { position: absolute; top: 70px; left: 0; right: 0; justify-content: center; }
  .cover__brand .brand__name { font-size: 20px; letter-spacing: 5px; }
  .cover__brand .brand__mark { width: 16px; height: 16px; }
  .cover__rule { position: absolute; left: 150px; right: 150px; top: 108px; height: 2px; background: var(--red); }
  .cover__band-line { position: absolute; left: 0; right: 0; bottom: 178px; height: 3px; background: var(--band-grey); }
  .cover__band {
    position: absolute; left: 0; right: 0; bottom: 0; height: 170px;
    background: linear-gradient(180deg, var(--red) 0%, var(--red-deep) 100%);
  }

  /* envelopes */
  .envelope-back { left: 880px; top: 50px; width: 290px; height: 150px; overflow: hidden; }
  .envelope-back__flap { position: absolute; inset: 0 0 auto 0; height: 62px; background: var(--ink); }
  .envelope-back__mark { position: absolute; left: 139px; top: 24px; width: 12px; height: 12px; background: var(--red); }

  .envelope-front { left: 880px; top: 230px; width: 290px; height: 150px; padding: 22px 20px; }
  .envelope-front__web { position: absolute; right: 20px; top: 24px; font-size: 6px; }
  .envelope-front__footer {
    position: absolute; left: 20px; right: 20px; bottom: 16px;
    border-top: 1px solid var(--red); padding-top: 5px;
  }

  /* business cards */
  .card { width: 260px; height: 150px; }
  .card--back { left: 880px; top: 420px; padding: 22px 20px; }
  .card__person { position: absolute; right: 20px; top: 22px; text-align: right; }
  .card__name { font-size: 9px; font-weight: 700; letter-spacing: .5px; text-transform: uppercase; white-space: nowrap; }
  .card__role { font-size: 6.4px; color: var(--grey-text); }
  .card__contact {
    position: absolute; left: 20px; right: 20px; bottom: 18px;
    border-top: 1px solid var(--red); padding-top: 5px;
  }
  .card--front { left: 880px; top: 600px; overflow: hidden; }
  .card--front .brand { position: absolute; left: 22px; top: 66px; }
  .card__corner {
    position: absolute; right: 0; top: 0; width: 90px; height: 150px;
    background: linear-gradient(180deg, var(--red), var(--red-deep));
  }
</style>
</head>
<body>

  <article class="sheet sheet--light letterhead">
    <div class="brand">
      <span class="brand__mark"></span>
      <span class="brand__name">Quorvane</span>
    </div>
    <p class="letterhead__salutation">Dear Sir / Madame,</p>
    <div class="letterhead__body">
      <p>Thank you for your continued interest in our software services. We build reliable tools that help IT departments of medium sized enterprises plan, deploy and support their systems with less effort and more clarity.</p>
      <p>Our team works closely with each client to understand daily needs, shape clear workflows and deliver updates on time. We would welcome the chance to discuss how we can support your next project.</p>
    </div>
    <p class="letterhead__closing">Kind regards,</p>
    <svg class="letterhead__signature" width="70" height="20" role="img" aria-label="Handwritten signature">
      <rect width="70" height="20" rx="3" fill="var(--signature-tint)"/>
    </svg>
    <p class="letterhead__signer">Tobin Rask</p>
    <footer class="letterhead__footer">
      <div class="contact-lines">
        27 Linden Row, Unit 8, Marlowe Falls, VT 05901<br>
        T: (555) 010-2716 &nbsp;F: (555) 010-2717 &nbsp;E: hello@quorvane.com
      </div>
      <span class="web">www.quorvanesoftware.com</span>
    </footer>
  </article>

  <article class="sheet sheet--dark cover">
    <div class="brand cover__brand">
      <span class="brand__mark"></span>
      <span class="brand__name">Quorvane</span>
    </div>
    <div class="cover__rule"></div>
    <div class="cover__band-line"></div>
    <div class="cover__band"></div>
  </article>

  <article class="sheet sheet--light envelope-back">
    <div class="envelope-back__flap"></div>
    <span class="envelope-back__mark"></span>
  </article>

  <article class="sheet sheet--light envelope-front">
    <div class="brand brand--small">
      <span class="brand__mark"></span>
      <span class="brand__name">Quorvane</span>
    </div>
    <span class="web envelope-front__web">www.quorvanesoftware.com</span>
    <footer class="envelope-front__footer contact-lines">
      27 Linden Row, Unit 8, Marlowe Falls, VT 05901<br>
      T: (555) 010-2716 &nbsp;F: (555) 010-2717 &nbsp;E: hello@quorvane.com
    </footer>
  </article>

  <article class="sheet sheet--light card card--back">
    <div class="brand brand--small">
      <span class="brand__mark"></span>
      <span class="brand__name">Quorvane</span>
    </div>
    <div class="card__person">
      <p class="card__name">Mara Lindqvist</p>
      <p class="card__role">Sales Manager</p>
    </div>
    <div class="card__contact contact-lines">
      27 Linden Row, Unit 8, Marlowe Falls, VT 05901<br>
      T: (555) 010-2716 &nbsp;F: (555) 010-2717 &nbsp;E: hello@quorvane.com
    </div>
  </article>

  <article class="sheet sheet--dark card card--front">
    <div class="card__corner"></div>
    <div class="brand">
      <span class="brand__mark"></span>
      <span class="brand__name">Quorvane</span>
    </div>
  </article>

</body>
</html>
```